Business card needed for home based pen making business.

I'm after a business card that's a bit more than an off the shelf card. I do like the idea of a card split horizontal with different colours used. A third colour is to be used for the business name and if need a forth for the other details.

I don't have a logo and will pay extra for one ($150 extra). I mainly make pens and seam rippers (stitch unpicks). The logo may be used for a website in future, as will the colours so please provide the colour codes and font type.

I'd like the business name in an easy to read script font at the top (with logo if you have one) and the other details to the bottom left hand side. I'll leave it up to you to match the script to the font used for the other details.

I'd like to keep a triangular balance to the card so something like a siloet of pot containing pens on the bottom right could be used to balance it out. There my ideas I want to see your.

Business name: Quill & Co
Email address: quillandco@mailbox-example.net
Contact: Trevor
Phone: 0412 555 874
No address is to be used on card.

Target Market(s)

Wide variety of people visiting craft markets. Age range 30+.

Industry/Entity Type

Business

Contact Information for Business Card

Quill & Co

Font styles to use
Script

Colors
f0ecf4
3277b5
3176b5

Requirements
Must have
• Contact: Trevor
• Phone: 0412 555 874
• Email address: quillandco@mailbox-example.net
Nice to have
• An icon and/or graphics depicting pens and seam rippers..
Should not have
• I don't want icon/ graphic to be a crossed pen and seam ripper.

```html
<!DOCTYPE html>
<html lang="en">
<head>
<meta charset="utf-8">
<title>Quill &amp; Co — Business Card</title>
<link rel="stylesheet" href="https://fonts.googleapis.com/css2?family=Marcellus&family=Cormorant+Garamond:ital,wght@1,600&family=Arimo&display=swap">
<style>
  :root {
    --page-bg: #d9d4cc;
    --card-top: #f4f3f4;
    --card-bottom: #e4e2e3;
    --name-blue-dark: #1f4f8c;
    --name-blue-light: #4a7db0;
    --band-grey: #7a7876;
    --band-blue-dark: #1f4e89;
    --band-blue-light: #3277b5;
    --contact-name: #ddd3c2;
    --contact-detail: #cfc2a6;
  }
  * { margin: 0; padding: 0; box-sizing: border-box; }
  html, body {
    width: 1200px;
    height: 970px;
    overflow: hidden;
    background: var(--page-bg);
  }
  .canvas {
    position: relative;
    width: 1200px;
    height: 970px;
  }
  .business-card {
    position: absolute;
    left: 100px;
    top: 185px;
    width: 1000px;
    height: 600px;
    background: linear-gradient(180deg, var(--card-top), var(--card-bottom));
    overflow: hidden;
    box-shadow: 0 6px 24px rgba(0, 0, 0, 0.18);
  }
  .card-waves {
    position: absolute;
    inset: 0;
    width: 1000px;
    height: 600px;
  }
  .business-name {
    position: absolute;
    left: 72px;
    top: 70px;
    font-family: "Marcellus", serif;
    font-size: 100px;
    line-height: 1.2;
    letter-spacing: 1px;
    background: linear-gradient(90deg, var(--name-blue-light), var(--name-blue-dark));
    -webkit-background-clip: text;
    background-clip: text;
    color: transparent;
  }
  .contact-block {
    position: absolute;
    right: 68px;
    top: 345px;
    text-align: right;
  }
  .contact-name {
    font-family: "Cormorant Garamond", serif;
    font-style: italic;
    font-weight: 600;
    font-size: 64px;
    line-height: 1;
    color: var(--contact-name);
    margin-bottom: 66px;
  }
  .contact-detail {
    font-family: "Arimo", sans-serif;
    font-size: 30px;
    line-height: 47px;
    color: var(--contact-detail);
  }
</style>
</head>
<body>
<main class="canvas">
  <section class="business-card">
    <svg class="card-waves" viewBox="0 0 1000 600" aria-hidden="true">
      <defs>
        <linearGradient id="band-blue" x1="0" y1="1" x2="1" y2="0">
          <stop offset="0" stop-color="var(--band-blue-light)"/>
          <stop offset="1" stop-color="var(--band-blue-dark)"/>
        </linearGradient>
      </defs>
      <path d="M90,600 C400,430 700,270 1000,255 L1000,600 Z" fill="var(--band-grey)" opacity="0.85"/>
      <path d="M300,600 C540,440 790,300 1000,297 L1000,600 Z" fill="url(#band-blue)"/>
    </svg>
    <h1 class="business-name">Quill &amp; Co</h1>
    <div class="contact-block">
      <p class="contact-name">Trevor</p>
      <p class="contact-detail">0412 555 874</p>
      <p class="contact-detail">quillandco@mailbox-example.net</p>
    </div>
  </section>
</main>
</body>
</html>
```